A6 Advertising Post Card

I am looking for refinement on this idea for an advertising letter-box drop of an A6 postcard.
Side 1 - our brand, the address, "15% discount if you present this card before Dec 31"

We are a new retail concept in terms of the store concept.

Side 2 - i want to highlight where the products are from, what materials are used, emphasis on cool, fresh, different, affordable, the product ranges grouped by colours (storage &organisation items in 1 colour or font, illumination products in 1 colour or font, furniture in 1 colour or font, decor in 1 colour or font, curios is 1 colour or font, fasion in 1 colour or font, others in a 1 colour or font)

The Product Categories:
see attachment

Hi

I've added the product categories with products sorted under each heading. I have also added the logo in a variety of file types (jpg, tif, psd, png). The sky blue background is part of the brand image.
Thanks

Target Market(s)

Home-makers (men and women) and women of all ages. Decision makers for home furnishings. Cross demographic - this is not premium..affordable to all social strata.
The brand is about fun, colourful and functional home stuff. The fashion stuff is a small percentage of the overall offer - targeting women who should spoil themselves as they spoil their families with nice stuff for the home.

Industry/Entity Type

Advertising

```html
<!DOCTYPE html>
<html lang="en">
<head>
<meta charset="utf-8">
<title>Kedai – A6 Postcard</title>
<link rel="stylesheet" href="https://fonts.googleapis.com/css2?family=Montserrat:wght@500;600;700&family=Didact+Gothic&display=swap">
<style>
  :root {
    --page: #d9d9d9;
    --card: #6fcbd6;
    --band: #4572b8;
    --header: #2e55a8;
    --white: #ffffff;
    --red: #e3262c;
    --navy: #1d4f7e;
    --coral: #f05a3a;
    --teal-dark: #063f3e;
    --purple: #6a58ad;
    --gold: #ecc64b;
    --ink: #17336b;
    --petal: #e7a3cf;
    --leaf: #5f9e52;
    --bloom: #f0a13a;
  }
  * { box-sizing: border-box; margin: 0; padding: 0; }
  html, body { width: 1200px; height: 795px; overflow: hidden; background: var(--page); }
  body { position: relative; font-family: "Didact Gothic", sans-serif; color: var(--white); }

  .spread {
    position: absolute; left: 14px; top: 186px;
    width: 1247px; height: 452px;
    transform: scale(0.94); transform-origin: top left;
  }
  .card { position: absolute; background: var(--card); overflow: hidden; }

  /* Side 1 */
  .card--front { left: 0; top: 9px; width: 597px; height: 432px; }
  .front__top-band {
    position: absolute; left: 0; top: 0; width: 100%; height: 22px;
    background: var(--band); font-size: 9px; letter-spacing: .6px;
    padding-left: 210px; line-height: 22px; color: #d6e4f5;
  }
  .brand { position: absolute; display: flex; align-items: center; gap: 10px; }
  .brand__dot { border-radius: 50%; background: var(--red); flex: none; }
  .brand__name { font-family: "Montserrat", sans-serif; font-weight: 700; color: var(--red); line-height: 1; }
  .brand__tagline { position: absolute; color: var(--ink); font-size: 17px; }
  .front .brand { left: 190px; top: 72px; }
  .front .brand__dot { width: 34px; height: 34px; }
  .front .brand__name { font-size: 64px; letter-spacing: 2px; }
  .front .brand__tagline { left: 265px; top: 50px; }

  .offer__badge {
    position: absolute; left: 258px; top: 173px; width: 92px; height: 92px;
    border-radius: 50%; background: var(--white); border: 2px solid var(--ink);
    display: flex; align-items: center; justify-content: center;
    font-family: "Montserrat", sans-serif; font-weight: 500; font-size: 36px; color: #111;
  }
  .offer__label {
    position: absolute; left: 150px; top: 264px; width: 310px; text-align: center;
    font-size: 29px; letter-spacing: .5px;
  }
  .offer__date {
    position: absolute; left: 178px; top: 302px; width: 249px; height: 25px;
    background: var(--red); text-align: center; line-height: 25px;
    font-family: "Montserrat", sans-serif; font-weight: 500; font-size: 16px; letter-spacing: 1px;
  }
  .info__lead { position: absolute; left: 178px; top: 340px; font-size: 14px; letter-spacing: .8px; }
  .info__web { position: absolute; left: 176px; top: 356px; font-size: 27px; letter-spacing: .8px; }
  .card__bottom-band {
    position: absolute; left: 0; bottom: 0; width: 100%; background: var(--band);
    text-align: center; font-size: 16px; letter-spacing: .8px;
  }
  .front .card__bottom-band { height: 27px; line-height: 27px; padding-left: 40px; }

  .art { position: absolute; }
  .art--blossoms {
    left: 0; top: 180px; width: 160px; height: 240px;
    background: radial-gradient(ellipse at 40% 55%, var(--petal) 0%, rgba(231,163,207,.45) 45%, rgba(111,203,214,0) 72%);
  }
  .art--vine {
    right: 0; top: 0; width: 130px; height: 240px;
    background: radial-gradient(ellipse at 60% 55%, var(--bloom) 0%, rgba(95,158,82,.55) 40%, rgba(111,203,214,0) 72%);
  }

  /* Side 2 */
  .card--back { left: 617px; top: 0; width: 630px; height: 452px; }
  .heading-bar {
    position: absolute; left: 40px; width: 560px; height: 22px; background: var(--header);
  }
  .heading-bar--top { top: 18px; }
  .heading-bar--lower { top: 285px; }
  .range { position: absolute; }
  .range__title {
    position: absolute; top: 0; white-space: nowrap;
    font-family: "Montserrat", sans-serif; font-weight: 600; font-size: 16px;
    line-height: 22px; letter-spacing: .3px;
  }
  .range__list { list-style: none; position: absolute; top: 26px; display: flex; flex-direction: column; gap: 1.7px; }
  .range__list li { height: 15px; line-height: 15px; padding-left: 4px; font-size: 11.5px; letter-spacing: .3px; white-space: nowrap; }

  .range--illumination li { background: var(--navy); }
  .range--curios li { background: var(--coral); }
  .range--decor li { background: var(--teal-dark); }
  .range--furniture li { background: var(--purple); color: var(--gold); }
  .range--fashion li { background: var(--purple); }
  .range--storage li { background: var(--teal-dark); }
  .range--misc li { background: var(--red); }
  .range--furniture li.two-line { height: 32px; line-height: 16px; }

  .back .brand { left: 50px; top: 220px; gap: 6px; }
  .back .brand__dot { width: 14px; height: 14px; }
  .back .brand__name { font-size: 28px; }
  .back .brand__tagline { left: 64px; top: 204px; font-size: 9px; }
  .back .card__bottom-band { height: 19px; line-height: 19px; font-size: 11px; letter-spacing: .6px; }
</style>
</head>
<body>
<main class="spread">

  <section class="card card--front front" aria-label="Postcard side 1">
    <div class="front__top-band">Copyright 2013. All Right Reserved.</div>
    <div class="art art--vine" role="img" aria-label="Trailing vine with orange blossoms"></div>
    <div class="art art--blossoms" role="img" aria-label="Scattered pink flowers with green swirls"></div>
    <p class="brand__tagline">A new store concept</p>
    <div class="brand"><span class="brand__dot"></span><span class="brand__name">Kedai</span></div>
    <div class="offer__badge">15%</div>
    <p class="offer__label">DISCOUNT EXPIRES</p>
    <p class="offer__date">31 DEC 2013</p>
    <p class="info__lead">For More Information Please Visit Us</p>
    <p class="info__web">www.kedaihome.com</p>
    <p class="card__bottom-band">42 Market Row, Elmfield</p>
  </section>

  <section class="card card--back back" aria-label="Postcard side 2">
    <div class="heading-bar heading-bar--top"></div>
    <div class="heading-bar heading-bar--lower"></div>

    <div class="range range--illumination" style="left:42px;top:18px">
      <h2 class="range__title">ILLUMINATION</h2>
      <ul class="range__list" style="width:113px">
        <li>Glass Votives</li><li>Lamps</li><li>Moroccan Lanterns</li><li>Chandeliers</li>
        <li>Candle Holders</li><li>Candles</li><li>Tee-light Holders</li><li>Pendant Lights</li><li>Lantern Stands</li>
      </ul>
    </div>

    <div class="range range--curios" style="left:185px;top:18px">
      <h2 class="range__title">CURIOS</h2>
      <ul class="range__list" style="width:133px">
        <li>Figurines</li><li>Brass Statues</li><li>Telescopes</li><li>Compasses</li><li>Gramophone</li>
        <li>Hour Glasses</li><li>Sextants</li><li>Magnifying Lens</li><li>Nepalese Prayer Wheels</li>
        <li>Nepalese Singing Bowls</li><li>Copper Incense Holder</li><li>Trumpet</li>
      </ul>
    </div>

    <div class="range range--decor" style="left:341px;top:18px">
      <h2 class="range__title">DECOR</h2>
      <ul class="range__list" style="width:132px">
        <li>Cushions</li><li>Photo-frames</li><li>Decorative Ornaments</li><li>Vases</li><li>Bowls</li>
        <li>Clocks</li><li>Mirrors</li><li>Bird Cages</li><li>Sedge Mats</li><li>Glass Decanters</li>
        <li>Pattachitra Bottles</li><li>Bird Cage Stands</li>
      </ul>
    </div>

    <div class="range range--furniture" style="left:495px;top:18px">
      <h2 class="range__title">FURNITURE</h2>
      <ul class="range__list" style="width:98px">
        <li>Cupboards</li><li>Tables</li><li>Stools</li><li>Chairs</li><li>Bookcases</li><li>Consoles</li>
        <li>Cart</li><li>Trolley</li><li class="two-line">Ceramic Knobs<br>&amp; Hooks</li><li>Ladders</li>
        <li>Umbrellas</li><li>Planters</li><li>Screen</li>
      </ul>
    </div>

    <p class="brand__tagline">A new store concept</p>
    <div class="brand"><span class="brand__dot"></span><span class="brand__name">Kedai</span></div>

    <div class="range range--fashion" style="left:42px;top:285px">
      <h2 class="range__title">FASHION</h2>
      <ul class="range__list" style="width:113px">
        <li>Shawls</li><li>Scarves</li><li>Mufflers</li><li>Bags</li><li>Bangles</li><li>Flip-Flops</li>
      </ul>
    </div>

    <div class="range range--storage" style="left:185px;top:285px">
      <h2 class="range__title">STORAGE &amp; ORGANISATION</h2>
      <ul class="range__list" style="width:79px">
        <li>Baskets</li><li>Trays</li><li>Drawers</li><li>Boxes</li><li>Tiffin Carrier</li><li>Plates</li>
      </ul>
      <ul class="range__list" style="left:98px;width:124px">
        <li>Bowls</li><li>Napkin Rings</li><li>Bamboo Towel Stands</li><li>Mugs</li><li>Cups</li><li>Water Jugs</li>
      </ul>
    </div>

    <div class="range range--misc" style="left:455px;top:285px">
      <h2 class="range__title">MISCELLANEOUS</h2>
      <ul class="range__list" style="width:145px">
        <li>Gift Bags</li><li>Wrapping Paper</li><li>Wine Bottle Holder</li><li>Xmas Decorations</li>
      </ul>
    </div>

    <p class="card__bottom-band">42 Market Row, Elmfield</p>
  </section>

</main>
</body>
</html>
```